Tour operator needs simple coded WordPress site (updated extra payment for coding and guaranteed)

[update 9/7/2015]
If you design a new logo and it gets accepted, even if we use another template with your logo you will get $50
[update 8/7/2015]
Update on questions about dual-language
For dual languages we are happy to set up a second site with the same designs in a second language.
For the design aspect just allow the user to switch between languages with an icon.
For the coding, a replica of the site on a second server will do (to save messing around with multiple language plugins) - we will populate it with Chinese text
[original post]
Simple coded WordPress site for tours
You can choose to design only or design and code ($340 design, $150 bonus for coding)
Open design brief - use your creativity
Will be in 2 languages (English and Chinese) but design needs only to be in one language
Winning design will be chosen only from home page, but the winner must make a second standard template page when chosen at no extra cost.
Must be responsive design
We only need homepage and standard template page design and coding, we will populate the pages
You can use design ideas from our pamphlet if you like - attached
Only a sample logo and colors on website and pamphlet - feel free to change as the current ones seem restrictive
Current website framework only to give an idea of the number of pages and basic menu structure (no need to use existing navigation style or any style at all for that matter, open brief)
http://brightwattlejourneys.com.au/
Target Market(s)
Chinese parents of kids 10-14 (the kids will take the tour)
Industry/Entity Type
Tour
Number of Pages Required
2 page
Look and feel
Each slider illustrates characteristics of the customer's brand and the style your logo design should communicate.

```html
<!DOCTYPE html>
<html lang="en">
<head>
<meta charset="utf-8">
<title>Bright Wattle Journeys</title>
<link href="https://fonts.googleapis.com/css2?family=Lato:wght@400;700&family=Oswald:wght@400;500&display=swap" rel="stylesheet">
<style>
:root{
  --navy:#2e3c82;
  --navy-band:#34458a;
  --gold:#f1b320;
  --ink:#333;
  --muted:#555;
  --line:#cfcfcf;
  --grey-bg:#eeeeef;
  --footer:#1c1c1c;
  --white:#fff;
}
*{box-sizing:border-box;margin:0;padding:0}
html,body{width:926px;height:1200px;overflow:hidden;background:var(--white)}
body{position:relative;font-family:'Lato',sans-serif;color:var(--ink)}
.abs{position:absolute}

/* hero */
.hero{position:absolute;left:0;top:0;width:926px;height:476px;
  background:linear-gradient(120deg,#3b4358 0%,#5a5a66 30%,#4a4e5e 55%,#2c3040 80%,#3a3a44 100%)}
.lang{left:748px;top:15px;width:77px;height:24px;border:2px solid var(--white);color:var(--white);
  font:700 12px 'Lato',sans-serif;display:flex;align-items:center;padding-left:9px;gap:10px}
.slide-arrow{top:200px}
.logo-box{left:101px;top:304px;width:216px;height:109px;background:var(--white);
  display:flex;align-items:center;justify-content:center;gap:8px}
.logo-dot{width:16px;height:16px;border-radius:50%;background:var(--gold)}
.logo-name{font:700 15px 'Lato',sans-serif;color:var(--navy);line-height:1.2}
.tagline{right:103px;top:362px;width:440px;text-align:right;color:var(--white);
  font:400 21px/28px 'Oswald',sans-serif;letter-spacing:-.2px;text-transform:uppercase}
.nav{left:0;top:429px;width:926px;height:47px;border-top:1px solid rgba(255,255,255,.45);background:rgba(20,22,30,.35)}
.nav a{position:absolute;top:0;height:47px;line-height:47px;color:var(--white);text-decoration:none;
  font:700 12px 'Lato',sans-serif;text-align:center}
.nav a.active{background:var(--white);color:var(--navy)}
.social{position:absolute;top:8px;width:30px;height:30px;border:2px solid var(--white);border-radius:50%}

/* intro */
.welcome{left:102px;top:520px;width:454px}
.h2{font:400 22px/30px 'Oswald',sans-serif;text-transform:uppercase;color:#2b2b2b;letter-spacing:-.3px}
.h2 .blue{color:var(--navy)} .h2 .gold{color:var(--gold)}
.welcome .h2{border-bottom:1px solid var(--line);padding-bottom:4px}
.lead{font:700 11.5px/15px 'Lato',sans-serif;color:#444;margin-top:8px}
.body{font:400 10px/13.5px 'Lato',sans-serif;color:var(--muted);margin-top:6px}
.btn{display:flex;align-items:center;justify-content:center;background:var(--navy);color:var(--white);
  font:700 14px 'Lato',sans-serif;text-transform:uppercase}
.divider{left:575px;top:506px;width:1px;height:210px;background:#e2e2e2}
.inquiry{left:598px;top:520px;width:227px}
.field{width:227px;height:26px;border:1px solid #c8c8c8;margin-top:7px;font:400 11px 'Lato',sans-serif;
  color:#999;padding:6px 7px}
.field.first{margin-top:9px}
.field.msg{height:58px}

/* features */
.features{left:0;top:733px;width:926px;height:380px;background:var(--grey-bg)}
.card{position:absolute;top:37px;width:348px;height:306px;background:var(--white);
  border:1px solid #d6d6d6;border-top:2px solid var(--gold);padding:14px 15px 0 14px}
.card-head{display:flex;align-items:flex-end;gap:8px;margin-bottom:10px}
.card-title{flex:1;font:400 17px/22px 'Oswald',sans-serif;color:var(--navy);text-transform:uppercase;
  border-bottom:1px dotted #aaa;letter-spacing:-.3px}
.card ul{list-style:none}
.card li{display:flex;gap:8px;font:400 10px/13px 'Lato',sans-serif;color:var(--muted);margin-bottom:6.5px}
.card li svg{flex:none;margin-top:1px}
.card.safe li{margin-bottom:5.5px}

/* newsletter */
.newsletter{left:0;top:1113px;width:926px;height:44px;background:var(--navy-band);color:var(--white)}
.nl-title{left:144px;top:9px;font:400 19px 'Lato',sans-serif}
.nl-sub{left:390px;top:15px;font:400 11.5px 'Lato',sans-serif}
.nl-input{left:571px;top:11px;width:189px;height:22px;background:var(--white);color:#333;
  font:400 10px 'Lato',sans-serif;padding:5px 7px}
.nl-btn{left:767px;top:11px;width:58px;height:22px;background:#111;border:1px solid #555;
  font:700 10px 'Lato',sans-serif;display:flex;align-items:center;justify-content:center}

/* footer */
.footer{left:0;top:1157px;width:926px;height:43px;background:var(--footer);color:var(--white);
  font:400 10px 'Lato',sans-serif}
.footer .links{left:102px;top:15px}
.footer .copy{right:102px;top:15px}
</style>
</head>
<body>

<header class="hero" role="img" aria-label="Photo of three smiling students studying together with a tablet and book in a campus cafeteria">
</header>

<div class="abs lang">English
  <svg width="11" height="7" viewBox="0 0 11 7"><path d="M1 1l4.5 4.5L10 1" fill="none" stroke="#fff" stroke-width="1.6"/></svg>
</div>
<svg class="abs slide-arrow" style="left:62px" width="40" height="78" viewBox="0 0 40 78"><path d="M39 1L1 39l38 38" fill="none" stroke="#fff" stroke-width="1"/></svg>
<svg class="abs slide-arrow" style="left:825px" width="40" height="78" viewBox="0 0 40 78"><path d="M1 1l38 38L1 77" fill="none" stroke="#fff" stroke-width="1"/></svg>

<div class="abs logo-box">
  <span class="logo-dot"></span>
  <span class="logo-name">Bright Wattle Journeys</span>
</div>

<h1 class="abs tagline">Educational, safe, culturally Bright Wattle Journeys enlightening and fun.</h1>

<nav class="abs nav">
  <a class="active" href="#" style="left:101px;width:112px">Home</a>
  <a href="#" style="left:236px;width:80px">About Us</a>
  <a href="#" style="left:356px;width:80px">Tours</a>
  <a href="#" style="left:480px;width:80px">Contact Us</a>
  <span class="social" style="left:714px" aria-label="Social link"></span>
  <span class="social" style="left:754px" aria-label="Social link"></span>
  <span class="social" style="left:794px" aria-label="Social link"></span>
</nav>

<section class="abs welcome">
  <h2 class="h2">Welcome to <span class="blue">Bright</span> <span class="gold">Wattle</span> <span class="blue">Journeys</span></h2>
  <p class="lead">At the Bright Wattle Journeys we are passionate about educational travel and opportunities for students to gain academic and cultural understanding of Australia.</p>
  <p class="body">14 day premium cultural and educational tours to Australian cities. Educational, safe, culturally enlightening and fun. Learn about educational institutions, history, sports, laws and customs, food and culture while improving your English.</p>
  <p class="body">At the Bright Wattle Journeys we are passionate about educational travel and providing opportunities for students to learn more about a country and gain a deeper understanding of the culture. The out of classroom experience gained on our trips is invaluable.</p>
</section>
<a class="abs btn" style="left:451px;top:690px;width:105px;height:26px;text-decoration:none">Read More</a>

<div class="abs divider"></div>

<section class="abs inquiry">
  <h2 class="h2">Quick Inquiry</h2>
  <div class="field first">Name</div>
  <div class="field">Email</div>
  <div class="field msg">Message</div>
</section>
<div class="abs btn" style="left:720px;top:690px;width:105px;height:26px">Submit</div>

<section class="abs features">
  <article class="card" style="left:101px">
    <div class="card-head">
      <svg width="30" height="20" viewBox="0 0 30 20"><path d="M15 2L1 8l14 6 14-6z" fill="#f1b320"/><path d="M7 11v5c3 3 13 3 16 0v-5l-8 3z" fill="#f1b320"/><path d="M27 9v7" stroke="#f1b320" stroke-width="1.5"/></svg>
      <h3 class="card-title">Educational and Cultural</h3>
    </div>
    <ul>
      <li><svg width="18" height="12" viewBox="0 0 18 12"><path d="M1 11C4 5 8 4 11 4V1l6 5-6 5V8C7 8 4 9 1 11z" fill="#2e3c82"/></svg>Professional lecturers from Sydney universities</li>
      <li><svg width="18" height="12" viewBox="0 0 18 12"><path d="M1 11C4 5 8 4 11 4V1l6 5-6 5V8C7 8 4 9 1 11z" fill="#2e3c82"/></svg>2 hour lessons every day in easy to understand,<br>high-quality English</li>
      <li><svg width="18" height="12" viewBox="0 0 18 12"><path d="M1 11C4 5 8 4 11 4V1l6 5-6 5V8C7 8 4 9 1 11z" fill="#2e3c82"/></svg>Subjects from the Australian Educational Curriculum as well as cultural information on Australia</li>
      <li><svg width="18" height="12" viewBox="0 0 18 12"><path d="M1 11C4 5 8 4 11 4V1l6 5-6 5V8C7 8 4 9 1 11z" fill="#2e3c82"/></svg>How to live, get around, shop and socialise in Australia</li>
      <li><svg width="18" height="12" viewBox="0 0 18 12"><path d="M1 11C4 5 8 4 11 4V1l6 5-6 5V8C7 8 4 9 1 11z" fill="#2e3c82"/></svg>Attitudes to languages, food, religion and culture</li>
      <li><svg width="18" height="12" viewBox="0 0 18 12"><path d="M1 11C4 5 8 4 11 4V1l6 5-6 5V8C7 8 4 9 1 11z" fill="#2e3c82"/></svg>Outdoor activities and sport</li>
    </ul>
  </article>

  <article class="card safe" style="left:477px">
    <div class="card-head">
      <svg width="34" height="24" viewBox="0 0 34 24"><path d="M6 10V7a6 6 0 0112 0v3" fill="none" stroke="#f1b320" stroke-width="2.5"/><rect x="2" y="10" width="20" height="14" rx="2" fill="#f1b320"/><circle cx="12" cy="16" r="2" fill="#fff"/></svg>
      <h3 class="card-title">Safe and Secure</h3>
    </div>
    <ul>
      <li><svg width="18" height="12" viewBox="0 0 18 12"><path d="M1 11C4 5 8 4 11 4V1l6 5-6 5V8C7 8 4 9 1 11z" fill="#2e3c82"/></svg>Staff certified by the government for Working With Children</li>
      <li><svg width="18" height="12" viewBox="0 0 18 12"><path d="M1 11C4 5 8 4 11 4V1l6 5-6 5V8C7 8 4 9 1 11z" fill="#2e3c82"/></svg>Staff certified in first aid care</li>
      <li><svg width="18" height="12" viewBox="0 0 18 12"><path d="M1 11C4 5 8 4 11 4V1l6 5-6 5V8C7 8 4 9 1 11z" fill="#2e3c82"/></svg>Professional accommodation with excellent history in caring for children with extremely well documented Safety Management Procedures including;</li>
      <li><svg width="18" height="12" viewBox="0 0 18 12"><path d="M1 11C4 5 8 4 11 4V1l6 5-6 5V8C7 8 4 9 1 11z" fill="#2e3c82"/></svg>Safety Management - reducing risk when taking students out of the classroom</li>
      <li><svg width="18" height="12" viewBox="0 0 18 12"><path d="M1 11C4 5 8 4 11 4V1l6 5-6 5V8C7 8 4 9 1 11z" fill="#2e3c82"/></svg>Safety &amp; Emergency Procedures (Location-specific)</li>
      <li><svg width="18" height="12" viewBox="0 0 18 12"><path d="M1 11C4 5 8 4 11 4V1l6 5-6 5V8C7 8 4 9 1 11z" fill="#2e3c82"/></svg>Standard Operating Procedures</li>
      <li><svg width="18" height="12" viewBox="0 0 18 12"><path d="M1 11C4 5 8 4 11 4V1l6 5-6 5V8C7 8 4 9 1 11z" fill="#2e3c82"/></svg>Activity-Specific Risk Management Matrix</li>
      <li><svg width="18" height="12" viewBox="0 0 18 12"><path d="M1 11C4 5 8 4 11 4V1l6 5-6 5V8C7 8 4 9 1 11z" fill="#2e3c82"/></svg>Area Assessment Documentation</li>
      <li><svg width="18" height="12" viewBox="0 0 18 12"><path d="M1 11C4 5 8 4 11 4V1l6 5-6 5V8C7 8 4 9 1 11z" fill="#2e3c82"/></svg>Medical Form, Dietary Requirements Form ,First Aid Incident &amp; Management Forms</li>
      <li><svg width="18" height="12" viewBox="0 0 18 12"><path d="M1 11C4 5 8 4 11 4V1l6 5-6 5V8C7 8 4 9 1 11z" fill="#2e3c82"/></svg>Clothing &amp; Equipment List</li>
    </ul>
  </article>
</section>

<section class="abs newsletter">
  <svg class="abs" style="left:101px;top:5px" width="34" height="34" viewBox="0 0 34 34"><circle cx="17" cy="17" r="15.5" fill="none" stroke="#fff" stroke-width="2"/><rect x="9" y="11" width="16" height="12" rx="1" fill="#fff"/><path d="M9.5 11.5L17 18l7.5-6.5" fill="none" stroke="#34458a" stroke-width="1.4"/></svg>
  <div class="abs nl-title">Newsletter Signup</div>
  <svg class="abs" style="left:344px;top:4px" width="28" height="36" viewBox="0 0 28 36"><path d="M2 2l14 16L2 34M10 2l14 16-14 16" fill="none" stroke="#fff" stroke-width="1.3"/></svg>
  <div class="abs nl-sub">Signup For Free Email Updates</div>
  <div class="abs nl-input">Enter your email here</div>
  <div class="abs nl-btn">SUBMIT</div>
</section>

<footer class="abs footer">
  <div class="abs links">Home &nbsp;|&nbsp; About Us &nbsp;|&nbsp; Tours &nbsp;|&nbsp; Contact Us</div>
  <div class="abs copy">© 2015 BRIGHT WATTLE JOURNEYS. &nbsp;|&nbsp; All Rights Reserved.</div>
</footer>

</body>
</html>
```